Updated Business Card Design more modern and eye catching

looking for something more dynamic than the sterile card we have now. Please take a look at our web site www.quarvinstores.net to see what we do. only looking for the front side of the card for now. I've also attached a sample of a card with raised spot uv ink - it might be cool to incorporate something like that. Card should be bold yet serious. No frilly or scrolly stuff on it.
Updates
Target Market(s)
We do decor and signage for retail business and supermarkets. Our new name should reflect that we're hip but serious.
Contact Information for Business Card
standard business card size - horizontal preferred
Font styles to use
Requirements
Must have
- Current logo and colors cannot be changed.
Nice to have
- Must have information shown on existing card but open to some changes. Okay to consider spot uv.
Should not have
- Not busy with pictures in the background.

```html
<!DOCTYPE html>
<html lang="en">
<head>
<meta charset="utf-8">
<title>Quarvin Stores – Business Card</title>
<link rel="stylesheet" href="https://fonts.googleapis.com/css2?family=Roboto:wght@400;500;700&display=swap">
<style>
  :root {
    --backdrop: #d9d9d9;
    --card: #1e1e1f;
    --card-edge: #2a2a2b;
    --gold: #c8b46a;
    --text: #f1f1f1;
    --spot-uv: #2b2b2c;
    --spot-uv-line: #3a3a3b;
  }
  * { box-sizing: border-box; margin: 0; padding: 0; }
  html, body {
    width: 1200px; height: 900px; overflow: hidden;
    background: var(--backdrop);
    font-family: "Roboto", Arial, sans-serif;
  }
  .business-card {
    position: absolute; left: 150px; top: 193px;
    width: 900px; height: 514px;
    background: var(--card);
    border: 1px solid var(--card-edge);
    color: var(--text);
  }
  .brand {
    position: absolute; left: 62px; top: 56px;
    display: flex; align-items: center; gap: 16px;
  }
  .brand-square {
    width: 40px; height: 40px;
    border: 3px solid var(--gold);
  }
  .brand-name {
    font-weight: 500; font-size: 34px; letter-spacing: 2px;
    color: var(--gold); text-transform: uppercase;
  }
  .holder { position: absolute; left: 62px; top: 140px; }
  .holder-name {
    font-size: 32px; font-weight: 500; letter-spacing: 1px; text-transform: uppercase;
  }
  .holder-first { color: var(--gold); font-weight: 700; }
  .holder-title { font-size: 20px; margin-top: 4px; }
  .holder-rule {
    width: 190px; height: 2px; background: var(--gold); margin-top: 16px;
  }
  .contact-list {
    position: absolute; left: 62px; top: 262px;
    list-style: none; font-size: 22px; line-height: 31px; letter-spacing: 0.5px;
  }
  .contact-item { display: flex; align-items: flex-start; gap: 14px; }
  .contact-icon { width: 22px; height: 22px; margin-top: 4px; flex: none; fill: var(--gold); }
  .extension { color: var(--gold); }
  .spot-uv-mark {
    position: absolute; left: 495px; top: 82px;
    width: 350px; height: 350px;
  }
</style>
</head>
<body>
  <article class="business-card">
    <header class="brand">
      <span class="brand-square"></span>
      <span class="brand-name">Quarvin Stores</span>
    </header>

    <section class="holder">
      <h1 class="holder-name"><span class="holder-first">Mara</span> Delling</h1>
      <p class="holder-title">Vice-President</p>
      <div class="holder-rule"></div>
    </section>

    <ul class="contact-list">
      <li class="contact-item">
        <svg class="contact-icon" viewBox="0 0 24 24"><path d="M3 8c0-3 4-4 9-4s9 1 9 4v2h-5V8H8v2H3z"/><path d="M6 12h12l2 8H4z"/><circle cx="12" cy="16" r="2" fill="#1e1e1f"/></svg>
        <span>555 204 7781 <span class="extension">ext. 3</span></span>
      </li>
      <li class="contact-item">
        <svg class="contact-icon" viewBox="0 0 24 24"><path d="M7 2h10a1 1 0 0 1 1 1v18a1 1 0 0 1-1 1H7a1 1 0 0 1-1-1V3a1 1 0 0 1 1-1zm1 3v13h8V5z"/></svg>
        <span>555 349 6610</span>
      </li>
      <li class="contact-item">
        <svg class="contact-icon" viewBox="0 0 24 24"><path d="M2 5h20v2l-10 6L2 7z"/><path d="M2 9l10 6 10-6v10H2z"/></svg>
        <span>maraj@quarvinstores.net</span>
      </li>
      <li class="contact-item">
        <svg class="contact-icon" viewBox="0 0 24 24"><circle cx="12" cy="12" r="10"/><path d="M7 7c2 0 3 1 3 3s-2 2-2 4 1 3 0 5M14 4c0 2 2 3 4 3M13 13c2 0 4 1 4 4" stroke="#1e1e1f" stroke-width="1.6" fill="none"/></svg>
        <span>www.quarvinstores.net</span>
      </li>
      <li class="contact-item">
        <svg class="contact-icon" viewBox="0 0 24 24"><path d="M12 2a7 7 0 0 1 7 7c0 5-7 13-7 13S5 14 5 9a7 7 0 0 1 7-7zm0 4a3 3 0 1 0 0 6 3 3 0 0 0 0-6z"/></svg>
        <span>4120 Commerce Loop<br>Dr Harlow Bay, FL 30417</span>
      </li>
    </ul>

    <svg class="spot-uv-mark" viewBox="0 0 350 350" aria-hidden="true">
      <circle cx="175" cy="175" r="170" fill="var(--spot-uv)" stroke="var(--spot-uv-line)" stroke-width="4"/>
    </svg>
  </article>
</body>
</html>
```